Standard logo business card

We are seeking a solid, somewhat understated professional design. We are a tech company. We like fonts similar to Aptifer Slab. Front side will be white with the contact information and a small version of our primary (Light background) logo.

(We have three people so we will have three names and titles)

Back side will hold our reverse logo on dark background along with the tagline:

"Intelligent annotation solutions for complex data"

Target Market(s)

Professionals, Tech

Industry/Entity Type

Business

Contact Information for Business Card

Name
Title

Phone
Email
City, State
Website

[We will email leading designer specific contact information)

Font styles to use
Serif

Requirements
Must have
• Colors are:
• Orange RGB 245,92,23
• Blue RGB 3,34,56
Nice to have
• We like a split with the Name and Title on the right and then contact details (below) on the left.

```html
<!DOCTYPE html>
<html lang="en">
<head>
<meta charset="utf-8">
<title>Corvanta business card</title>
<link href="https://fonts.googleapis.com/css2?family=PT+Sans:wght@400;700&display=swap" rel="stylesheet">
<style>
  :root {
    --orange: #f55c17;
    --navy: #032238;
    --green: #8cc63f;
    --green-light: #a3d45e;
    --white: #ffffff;
    --ink: #111111;
    --rule: #7f8790;
  }
  html, body {
    margin: 0;
    padding: 0;
    width: 1057px;
    height: 1200px;
    overflow: hidden;
    background: var(--white);
    font-family: "PT Sans", sans-serif;
  }
  .canvas { position: relative; width: 1057px; height: 1200px; }

  .card {
    position: absolute;
    left: 22px;
    width: 1013px;
    overflow: hidden;
    box-shadow: 6px 6px 8px rgba(0,0,0,0.25);
  }

  /* Front */
  .card-front { top: 0; height: 552px; background: var(--white); }
  .brand {
    position: absolute;
    display: flex;
    align-items: center;
    gap: 12px;
    font-weight: 700;
    color: var(--navy);
    line-height: 1;
  }
  .brand-mark { display: block; background: var(--orange); }
  .card-front .brand { left: 38px; top: 26px; font-size: 52px; }
  .card-front .brand-mark { width: 30px; height: 30px; }

  .person { position: absolute; left: 218px; width: 196px; }
  .person-name {
    display: block;
    text-align: center;
    font-size: 36px;
    color: var(--navy);
    line-height: 1;
    padding-bottom: 4px;
    border-bottom: 2px solid var(--rule);
  }
  .person-role {
    display: block;
    margin-left: 44px;
    margin-top: 6px;
    font-size: 24px;
    font-weight: 700;
    color: var(--navy);
    line-height: 1;
  }
  .person-1 { top: 136px; }
  .person-2 { top: 222px; }
  .person-3 { top: 320px; }

  .divider { position: absolute; left: 496px; top: 128px; }

  .contact {
    position: absolute;
    left: 571px;
    font-size: 28px;
    color: var(--ink);
    line-height: 1;
  }
  .contact-1 { top: 156px; }
  .contact-2 { top: 238px; }
  .contact-3 { top: 344px; }

  .band-navy { position: absolute; left: 0; width: 100%; background: var(--navy); }
  .band-green { position: absolute; left: 0; width: 100%; background: var(--green); }
  .card-front .band-navy { top: 441px; height: 23px; }
  .card-front .band-green { top: 464px; height: 88px; }

  .footer-item {
    position: absolute;
    display: flex;
    align-items: center;
    gap: 22px;
    color: var(--white);
    font-weight: 700;
  }
  .address { left: 70px; top: 472px; font-size: 19px; line-height: 22px; }
  .website { left: 560px; top: 492px; font-size: 20px; }

  /* Back */
  .card-back { top: 640px; height: 525px; background: var(--green); }
  .card-back .brand { left: 32px; top: 26px; font-size: 28px; color: var(--white); gap: 8px; }
  .card-back .brand-mark { width: 16px; height: 16px; background: var(--white); }
  .brand-watermark {
    position: absolute;
    left: 0;
    width: 100%;
    top: 92px;
    text-align: center;
    font-size: 170px;
    font-weight: 700;
    color: var(--green-light);
    line-height: 1;
  }
  .tagline {
    position: absolute;
    left: 0;
    width: 100%;
    top: 230px;
    text-align: center;
    font-size: 40px;
    color: var(--ink);
    margin: 0;
  }
  .band-white { position: absolute; left: 0; width: 100%; top: 450px; height: 13px; background: var(--white); }
  .card-back .band-navy { top: 463px; height: 22px; }
  .card-back .band-green { top: 485px; height: 40px; }
</style>
</head>
<body>
<div class="canvas">

  <section class="card card-front">
    <div class="brand"><span class="brand-mark"></span>corvanta</div>

    <div class="person person-1"><span class="person-name">Name</span><span class="person-role">position</span></div>
    <div class="person person-2"><span class="person-name">Name</span><span class="person-role">position</span></div>
    <div class="person person-3"><span class="person-name">Name</span><span class="person-role">position</span></div>

    <svg class="divider" width="8" height="282" viewBox="0 0 8 282">
      <path d="M4 0 L6 141 L4 282 L2 141 Z" fill="var(--orange)"/>
    </svg>

    <div class="contact contact-1">contact number</div>
    <div class="contact contact-2">contact number</div>
    <div class="contact contact-3">contact number</div>

    <div class="band-navy"></div>
    <div class="band-green"></div>

    <div class="footer-item address">
      <svg width="44" height="30" viewBox="0 0 44 30" fill="none" stroke="var(--white)" stroke-width="3">
        <path d="M3 15 L22 3 L41 15"/>
        <path d="M10 13 V27 H34 V13"/>
      </svg>
      <span>B-7-12 Harbour Court,<br>Jalan Meru 4,<br>41050 Klang, Malaysia</span>
    </div>

    <div class="footer-item website">
      <svg width="44" height="32" viewBox="0 0 44 32" fill="none" stroke="var(--white)" stroke-width="2.5">
        <rect x="3" y="3" width="38" height="26" rx="3"/>
        <ellipse cx="22" cy="16" rx="8" ry="11"/>
        <path d="M3 16 H41 M22 3 V29"/>
      </svg>
      <span>http://northlineworks.com</span>
    </div>
  </section>

  <section class="card card-back">
    <div class="brand"><span class="brand-mark"></span>corvanta</div>
    <div class="brand-watermark" aria-hidden="true">corvanta</div>
    <p class="tagline">"Intelligent annotation solutions for complex data"</p>
    <div class="band-white"></div>
    <div class="band-navy"></div>
    <div class="band-green"></div>
  </section>

</div>
</body>
</html>
```